Website redesign for job agency recruitment

Please refer to the attached document, “Harbor Work Portal Outline,” for comprehensive details regarding the scope, objectives, and requirements of this website redesign project.

For imagery you can use images from this website https://www.pixvaultmedia.com or any other you regularly use.

Target Market(s)

Jobseekers and Companies looking for general labour

Industry/Entity Type

Services: Oil, Gas and Mining, Administrative, Construction and Trades, Warehouse and Logistics and, Manufacturing.

Number of Pages Required

5+ page

Font styles to use
Serif
Other font styles liked:
• Inter, Open-Sans or similar.

Requirements
Must have
• The requirements highlighted in the Word document attached. The final design needs to be provided in Figma including all viewports (Desktop, mobiel and tablet)
Should not have
• Website we like as a reference: www.beltonworkforceinc.com, www.veltaworkforce.com, www.zplacer.com, www.brimwellworkforce.com, www.9tworkcrew.com, www.hiringonthemove.ca

```html
<!DOCTYPE html>
<html lang="en">
<head>
<meta charset="utf-8">
<title>Harbor Work Agency – Recruitment</title>
<link rel="stylesheet" href="https://fonts.googleapis.com/css2?family=Inter:ital,wght@0,400;0,500;0,600;0,700;0,800;1,400&display=swap">
<style>
:root{
  --gold:#f5b50a;
  --gold-dark:#b8860b;
  --navy:#1c2560;
  --ink:#111827;
  --deep:#121936;
  --muted:#6b7280;
  --line:#e6e9ef;
  --soft:#f5f7fb;
  --mist:#edf1f8;
  --white:#ffffff;
}
*{box-sizing:border-box;margin:0;padding:0}
html,body{width:1200px;height:3052px;overflow:hidden}
body{font-family:'Inter',sans-serif;color:var(--ink);background:var(--white);position:relative}
.abs{position:absolute}
.eyebrow{font-size:8.5px;font-weight:600;letter-spacing:1px;color:var(--gold-dark);text-transform:uppercase}
.h2{font-size:24px;font-weight:700;color:var(--ink);letter-spacing:-.3px}
.btn{display:inline-flex;align-items:center;justify-content:center;border-radius:4px;font-size:11px;font-weight:500;white-space:nowrap}
.btn-gold{background:var(--gold);color:var(--ink)}
.btn-line{border:1px solid var(--navy);color:var(--navy);background:var(--white)}

/* Header */
.site-header{position:absolute;left:0;top:0;width:1200px;height:50px}
.brand{left:180px;top:13px;display:flex;align-items:center;gap:6px}
.brand-dot{width:20px;height:20px;border-radius:50%;background:var(--navy)}
.brand-name{font-size:10.5px;font-weight:600;color:var(--navy);white-space:nowrap}
.main-nav{left:369px;top:19px;display:flex;gap:21px;font-size:9px;color:#374151;white-space:nowrap}
.nav-cta{top:15px;height:21px;font-size:8.5px;padding:0}

/* Hero */
.hero{left:47px;top:50px;width:1105px;height:557px;border-radius:0 0 14px 14px;overflow:hidden;
  background:linear-gradient(160deg,#c9d3de 0%,#7d8a99 30%,#2a3038 55%,#181c22 75%,#3a3126 100%)}
.hero-shade{position:absolute;inset:0;background:radial-gradient(ellipse at 50% 50%,rgba(0,0,0,.25),rgba(0,0,0,0) 60%)}
.hero-title{left:0;width:1105px;top:222px;text-align:center;font-size:45px;font-weight:800;color:#fff;line-height:1;letter-spacing:-.5px}
.hero-sub{left:0;width:1105px;top:326px;text-align:center;font-size:15px;color:#f1f3f5;line-height:20px}
.hero-actions{left:0;width:1105px;top:392px;display:flex;justify-content:center;gap:10px}
.hero-actions .btn{height:35px;font-size:12px;padding:0 20px}
.hero-actions .btn-ghost{border:1px solid #fff;color:#fff}
.dots{left:0;width:1105px;top:505px;display:flex;justify-content:center;gap:7px;align-items:center}
.dots i{width:7px;height:7px;border-radius:50%;background:rgba(255,255,255,.6)}
.dots i.on{width:20px;border-radius:4px;background:var(--gold)}

/* Expertise */
.section-head{left:0;width:1200px;text-align:center}
.section-head p{font-size:10.5px;color:#4b5563;line-height:15px}
.acc{left:220px;width:364px;border:1px solid var(--line);border-radius:6px;background:#fff}
.acc-row{position:absolute;left:14px;top:16px;display:flex;gap:10px;width:334px}
.acc-icon{width:24px;height:24px;border-radius:5px;background:#f1f3f7;display:flex;align-items:center;justify-content:center;flex:none}
.acc-title{font-size:11.5px;font-weight:600;color:var(--ink)}
.acc-desc{font-size:8.5px;color:var(--muted);margin-top:4px}
.chev{position:absolute;right:16px;top:24px}
.acc.open{background:var(--soft);border-color:#b8c4da}
.acc.open .acc-icon{background:var(--navy)}
.acc.open .acc-desc{color:#374151}
.acc-body{position:absolute;left:14px;top:62px;width:330px;font-size:9.8px;line-height:16.5px;color:#4b5563}
.acc-link{position:absolute;left:14px;top:140px;font-size:10px;color:var(--gold-dark);font-weight:500}
.feature-card{left:615px;top:782px;width:365px;height:373px;border-radius:8px;overflow:hidden;box-shadow:0 10px 24px rgba(0,0,0,.18);
  background:linear-gradient(180deg,#9aa1a6 0%,#7d7467 35%,#8c7e6c 60%,#3b3a3a 85%,#1a1a1a 100%)}
.feature-card h3{position:absolute;left:20px;top:268px;font-size:19px;font-weight:700;color:#fff}
.feature-card p{position:absolute;left:20px;top:297px;font-size:10px;color:#e5e7eb}
.feature-card .btn{position:absolute;left:20px;top:327px;height:27px;padding:0 12px;font-size:10px}

/* About */
.about{left:0;top:1294px;width:1200px;height:443px;background:var(--soft)}
.photo{border-radius:6px;box-shadow:0 8px 20px rgba(0,0,0,.12)}
.stat-card{left:419px;top:234px;width:175px;height:90px;background:#fff;border-radius:6px;box-shadow:0 8px 22px rgba(0,0,0,.12)}
.stat-badge{position:absolute;left:15px;top:14px;width:30px;height:30px;border-radius:50%;background:#fdf1cc;color:var(--gold-dark);font-size:11px;font-weight:700;display:flex;align-items:center;justify-content:center}
.about-copy{left:620px;top:56px;width:360px}
.about-copy h2{font-size:24px;line-height:25px;margin-top:6px;font-weight:700;letter-spacing:-.3px}
.about-copy .lead{font-size:11px;line-height:18.2px;color:#4b5563;margin-top:14px}
.checks{margin-top:12px;display:flex;flex-direction:column;gap:15px}
.check{display:flex;gap:9px}
.check b{display:block;font-size:10px;font-weight:600}
.check span{display:block;font-size:8.5px;color:var(--muted);margin-top:3px}
.about-actions{display:flex;gap:11px;margin-top:20px}
.about-actions .btn{height:27px;padding:0 13px;font-size:10px}

/* Values */
.values{left:0;top:1737px;width:1200px;height:426px;background:var(--mist)}
.value-card{top:175px;width:174px;height:201px;background:#fff;border-radius:6px;text-align:center;padding:0 20px}
.value-icon{width:40px;height:40px;border-radius:50%;background:#e3e9f5;margin:20px auto 0;display:flex;align-items:center;justify-content:center}
.value-card h3{font-size:13px;font-weight:600;margin-top:14px;white-space:nowrap}
.value-card p{font-size:10px;line-height:16.3px;color:var(--muted);margin-top:9px}

/* Testimonials */
.quote-card{top:2304px;width:245px;height:172px;border-bottom:1px solid #f0f1f4;padding:18px 20px}
.stars{display:flex;gap:2px}
.quote-mark{position:absolute;right:14px;top:8px;font-size:44px;font-weight:700;color:#dfe4ee;line-height:1}
.quote-card q{display:block;font-size:10px;font-style:italic;line-height:15.2px;color:#4b5563;margin-top:14px;quotes:none}
.quote-name{position:absolute;left:20px;top:136px;font-size:10px;font-weight:600}
.quote-role{position:absolute;left:20px;top:150px;font-size:8.5px;color:var(--muted);white-space:nowrap}

/* CTA */
.cta-seek{left:0;top:2539px;width:600px;height:218px;background:var(--deep)}
.cta-hire{left:600px;top:2539px;width:600px;height:218px;background:var(--gold)}
.cta-seek .inner{position:absolute;right:30px;top:56px;text-align:right;width:320px}
.cta-hire .inner{position:absolute;left:30px;top:55px;width:320px}
.cta-block h2{font-size:19px;font-weight:700;white-space:nowrap}
.cta-block p{font-size:10px;line-height:14.5px;margin-top:10px}
.cta-block .btn{height:34px;padding:0 20px;font-size:11.5px;margin-top:21px}

/* Footer */
.site-footer{left:0;top:2757px;width:1200px;height:295px;background:var(--deep);color:#c7cbd6}
.foot-brand{position:absolute;left:220px;top:47px}
.foot-brand strong{font-size:14px;font-weight:800;color:#fff;letter-spacing:-.2px}
.foot-brand small{display:block;font-size:5.5px;letter-spacing:1px;color:#aeb4c4;margin-top:1px}
.foot-about{position:absolute;left:220px;top:84px;width:160px;font-size:8.8px;line-height:14.5px}
.socials{position:absolute;left:220px;top:162px;display:flex;gap:12px}
.socials i{width:23px;height:23px;border-radius:50%;background:#232b4d}
.foot-col{position:absolute;top:49px}
.foot-col h4{font-size:10.5px;font-weight:600;color:#fff}
.foot-col ul{list-style:none;margin-top:15px;display:flex;flex-direction:column;gap:10px;font-size:9.5px;white-space:nowrap}
.foot-contact li{display:flex;gap:9px;font-size:8.8px;line-height:12.5px}
.foot-bottom{position:absolute;left:220px;top:252px;width:760px;border-top:1px solid #242c4c;padding-top:14px;display:flex;justify-content:space-between;font-size:8.5px;color:#8b92a8}
.foot-bottom nav{display:flex;gap:16px}
</style>
</head>
<body>

<header class="site-header">
  <div class="abs brand"><span class="brand-dot"></span><span class="brand-name">Harbor Work Agency Ltd.</span></div>
  <nav class="abs main-nav">
    <span>Home</span><span>About Us</span><span>Services ⌄</span><span>Candidates</span><span>Employers</span><span>Vancouver</span><span>Contact</span>
  </nav>
  <span class="abs btn btn-gold nav-cta" style="left:815px;width:79px">For Candidates</span>
  <span class="abs btn btn-line nav-cta" style="left:903px;width:77px">For Employers</span>
</header>

<section class="abs hero" role="img" aria-label="Upward view of glass office towers against a cloudy sky">
  <div class="hero-shade"></div>
  <h1 class="abs hero-title">Your Career, Our<br>Commitment</h1>
  <p class="abs hero-sub">Connecting ambitious professionals with Canada's top<br>employers.</p>
  <div class="abs hero-actions">
    <span class="btn btn-gold">Find Jobs</span>
    <span class="btn btn-ghost">Hire Talent</span>
  </div>
  <div class="abs dots"><i class="on"></i><i></i><i></i></div>
</section>

<section>
  <div class="abs section-head" style="top:659px">
    <div class="eyebrow">Our Expertise</div>
    <h2 class="h2" style="margin-top:8px">Specialized Recruitment Services</h2>
    <p style="margin-top:9px">We provide tailored staffing solutions across key industries, ensuring the perfect match<br>for both employers and job seekers.</p>
  </div>

  <div class="abs acc" style="top:782px;height:62px">
    <div class="acc-row"><span class="acc-icon"><svg width="12" height="12" viewBox="0 0 12 12" fill="none" stroke="#6b7280" stroke-width="1"><rect x="2" y="2" width="8" height="9"/><path d="M4 4h1M7 4h1M4 6h1M7 6h1M5 11V9h2v2"/></svg></span>
      <div><div class="acc-title">Oil, Gas &amp; Mining</div><div class="acc-desc">Specialized recruitment for the energy and resource sectors.</div></div></div>
    <svg class="chev" width="9" height="9" viewBox="0 0 9 9"><path d="M2 3.5l2.5 2.5L7 3.5" fill="none" stroke="#9ca3af" stroke-width="1"/></svg>
  </div>
  <div class="abs acc" style="top:855px;height:62px">
    <div class="acc-row"><span class="acc-icon"><svg width="12" height="12" viewBox="0 0 12 12" fill="none" stroke="#6b7280" stroke-width="1"><circle cx="4.5" cy="4" r="2"/><path d="M1 10c0-2 1.5-3 3.5-3s3.5 1 3.5 3M8 2.2a2 2 0 010 3.6M9.5 7.2c1 .5 1.5 1.4 1.5 2.8"/></svg></span>
      <div><div class="acc-title">Administrative</div><div class="acc-desc">Office support and administrative professionals for all industries.</div></div></div>
    <svg class="chev" width="9" height="9" viewBox="0 0 9 9"><path d="M2 3.5l2.5 2.5L7 3.5" fill="none" stroke="#9ca3af" stroke-width="1"/></svg>
  </div>
  <div class="abs acc open" style="top:929px;height:168px">
    <div class="acc-row"><span class="acc-icon"><svg width="12" height="12" viewBox="0 0 12 12" fill="none" stroke="#fff" stroke-width="1"><path d="M2 8a4 4 0 018 0M1 8h10v1.5H1zM6 4v2"/></svg></span>
      <div><div class="acc-title">Construction &amp; Trades</div><div class="acc-desc">Skilled tradespeople and construction management staff.</div></div></div>
    <svg class="chev" width="9" height="9" viewBox="0 0 9 9"><path d="M2 5.5L4.5 3 7 5.5" fill="none" stroke="#374151" stroke-width="1"/></svg>
    <p class="acc-body">We understand the urgency of construction timelines. Our database includes qualified carpenters, electricians, plumbers, site superintendents, and project managers ready to hit the ground running on your commercial or residential projects.</p>
    <span class="acc-link">Learn More →</span>
  </div>
  <div class="abs acc" style="top:1106px;height:62px">
    <div class="acc-row"><span class="acc-icon"><svg width="12" height="12" viewBox="0 0 12 12" fill="none" stroke="#6b7280" stroke-width="1"><path d="M1 3h6v5H1zM7 5h2.5L11 7v1H7"/><circle cx="3" cy="9" r="1"/><circle cx="9" cy="9" r="1"/></svg></span>
      <div><div class="acc-title">Warehouse &amp; Logistics</div><div class="acc-desc">Efficient staffing for supply chain and distribution centers.</div></div></div>
    <svg class="chev" width="9" height="9" viewBox="0 0 9 9"><path d="M2 3.5l2.5 2.5L7 3.5" fill="none" stroke="#9ca3af" stroke-width="1"/></svg>
  </div>
  <div class="abs acc" style="top:1180px;height:63px">
    <div class="acc-row"><span class="acc-icon"><svg width="12" height="12" viewBox="0 0 12 12" fill="none" stroke="#6b7280" stroke-width="1"><path d="M1.5 10.5V2h2v4l3-2v2l3-2v6.5z"/></svg></span>
      <div><div class="acc-title">Manufacturing</div><div class="acc-desc">Production and assembly talent for the manufacturing sector.</div></div></div>
    <svg class="chev" width="9" height="9" viewBox="0 0 9 9"><path d="M2 3.5l2.5 2.5L7 3.5" fill="none" stroke="#9ca3af" stroke-width="1"/></svg>
  </div>

  <div class="abs feature-card" role="img" aria-label="Construction site with rebar grid and a crew in safety vests">
    <h3>Construction &amp; Trades</h3>
    <p>Skilled tradespeople and construction management staff.</p>
    <span class="btn btn-gold">Explore Construction &amp; Trades</span>
  </div>
</section>

<section class="abs about">
  <div class="abs photo" style="left:220px;top:151px;width:175px;height:160px;background:linear-gradient(135deg,#6b5a48,#3d3a38 50%,#8a7b6a)" role="img" aria-label="Team collaborating around laptops at a shared table"></div>
  <div class="abs photo" style="left:406px;top:131px;width:174px;height:162px;background:linear-gradient(135deg,#eceae6,#d8d4cc 55%,#b7a99b)" role="img" aria-label="Colleague arranging sticky notes on a whiteboard"></div>
  <div class="abs stat-card">
    <span class="stat-badge">15+</span>
    <div class="abs" style="left:55px;top:16px;font-size:10px;font-weight:600;white-space:nowrap">Years Experience</div>
    <div class="abs" style="left:55px;top:30px;font-size:7.5px;color:var(--muted);white-space:nowrap">Serving Canadian Businesses</div>
    <div class="abs" style="left:15px;top:57px;font-size:8.5px;color:#4b5563">Client Satisfaction</div>
    <div class="abs" style="right:15px;top:57px;font-size:8.5px;font-weight:600;color:var(--navy)">98%</div>
    <div class="abs" style="left:15px;top:72px;width:145px;height:4px;border-radius:2px;background:var(--gold)"></div>
  </div>

  <div class="abs about-copy">
    <div class="eyebrow">Who We Are</div>
    <h2>Building Bridges Between Talent and Opportunity</h2>
    <p class="lead">Harbor Work is a premier recruitment agency dedicated to connecting exceptional talent with leading organizations across Canada. With over 15 years of industry experience, we understand that every placement is about more than just skills—it's about people.</p>
    <div class="checks">
      <div class="check"><svg width="13" height="13" viewBox="0 0 13 13"><circle cx="6.5" cy="6.5" r="5.7" fill="none" stroke="#d9a20a" stroke-width="1"/><path d="M4 6.7l1.7 1.6L9 5" fill="none" stroke="#d9a20a" stroke-width="1"/></svg><div><b>Personalized Approach</b><span>We take the time to understand your unique needs and culture.</span></div></div>
      <div class="check"><svg width="13" height="13" viewBox="0 0 13 13"><circle cx="6.5" cy="6.5" r="5.7" fill="none" stroke="#d9a20a" stroke-width="1"/><path d="M4 6.7l1.7 1.6L9 5" fill="none" stroke="#d9a20a" stroke-width="1"/></svg><div><b>Industry Specialists</b><span>Our recruiters are experts in their specific verticals.</span></div></div>
      <div class="check"><svg width="13" height="13" viewBox="0 0 13 13"><circle cx="6.5" cy="6.5" r="5.7" fill="none" stroke="#d9a20a" stroke-width="1"/><path d="M4 6.7l1.7 1.6L9 5" fill="none" stroke="#d9a20a" stroke-width="1"/></svg><div><b>Nationwide Network</b><span>Access to a vast pool of candidates and employers across Canada.</span></div></div>
    </div>
    <div class="about-actions"><span class="btn btn-gold">Learn More About Us</span><span class="btn btn-line">Contact Us</span></div>
  </div>
</section>

<section class="abs values">
  <div class="abs section-head" style="top:56px">
    <div class="eyebrow">Our Value</div>
    <h2 class="h2" style="margin-top:8px">Why Choose Harbor Work</h2>
    <p style="margin-top:9px">We go beyond traditional recruitment to deliver exceptional results for both candidates<br>and employers.</p>
  </div>
  <div class="abs value-card" style="left:220px">
    <div class="value-icon"><svg width="18" height="18" viewBox="0 0 18 18" fill="none" stroke="#1c2560" stroke-width="1.3"><rect x="2.5" y="5.5" width="13" height="10" rx="1.5"/><path d="M6.5 5.5V3.5h5v2M6.5 5.5v10M11.5 5.5v10"/></svg></div>
    <h3>Industry Expertise</h3>
    <p>Our recruiters are specialists in their fields, understanding the unique requirements and trends of your industry.</p>
  </div>
  <div class="abs value-card" style="left:415px">
    <div class="value-icon"><svg width="18" height="18" viewBox="0 0 18 18" fill="none" stroke="#1c2560" stroke-width="1.3"><circle cx="7" cy="6" r="3"/><path d="M2 15c0-3 2.2-4.5 5-4.5s5 1.5 5 4.5M12 3.3a3 3 0 010 5.4M14 11c1.3.7 2 1.9 2 4"/></svg></div>
    <h3>Personalized Service</h3>
    <p>We believe in building relationships, not just filling roles. We take a tailored approach to every placement.</p>
  </div>
  <div class="abs value-card" style="left:610px">
    <div class="value-icon"><svg width="18" height="18" viewBox="0 0 18 18" fill="none" stroke="#1c2560" stroke-width="1.3"><path d="M9 16s5-4.5 5-8.5a5 5 0 00-10 0C4 11.5 9 16 9 16z"/><circle cx="9" cy="7.5" r="1.8"/></svg></div>
    <h3>Nationwide Reach</h3>
    <p>With a strong presence across Canada, we can source talent and opportunities from coast to coast.</p>
  </div>
  <div class="abs value-card" style="left:805px">
    <div class="value-icon"><svg width="18" height="18" viewBox="0 0 18 18" fill="none" stroke="#1c2560" stroke-width="1.3" stroke-linejoin="round"><path d="M10 2L3.5 10.5H9L8 16l6.5-8.5H9z"/></svg></div>
    <h3>Fast Placement</h3>
    <p>Our efficient screening process ensures you get qualified candidates or job offers quickly without compromising quality.</p>
  </div>
</section>

<section>
  <div class="abs section-head" style="top:2216px">
    <div class="eyebrow">Testimonials</div>
    <h2 class="h2" style="margin-top:8px">What Our Clients Say</h2>
  </div>

  <article class="abs quote-card" style="left:220px">
    <div class="stars"><svg width="62" height="11" viewBox="0 0 62 11"><g fill="#f5b50a"><path id="st" d="M5.5 0l1.6 3.5 3.8.4-2.9 2.6.9 3.8-3.4-2-3.4 2 .9-3.8L.1 3.9l3.8-.4z"/><use href="#st" x="12.5"/><use href="#st" x="25"/><use href="#st" x="37.5"/><use href="#st" x="50"/></g></svg></div>
    <span class="quote-mark">”</span>
    <q>"Harbor Work understood our company culture perfectly. The candidates they presented were not just qualified, but a perfect fit for our team. We've hired three people through them this year."</q>
    <div class="quote-name">Maren Holloway</div>
    <div class="quote-role">HR Director, Brightline Systems</div>
  </article>
  <article class="abs quote-card" style="left:480px">
    <div class="stars"><svg width="62" height="11" viewBox="0 0 62 11"><g fill="#f5b50a"><use href="#st"/><use href="#st" x="12.5"/><use href="#st" x="25"/><use href="#st" x="37.5"/><use href="#st" x="50"/></g></svg></div>
    <span class="quote-mark">”</span>
    <q>"As a candidate, I felt supported throughout the entire process. They helped me refine my resume and prepared me for interviews. I landed my dream job within two weeks!"</q>
    <div class="quote-name">Owen Takeda</div>
    <div class="quote-role">Senior Project Manager, Ironridge Builders</div>
  </article>
  <article class="abs quote-card" style="left:740px">
    <div class="stars"><svg width="62" height="11" viewBox="0 0 62 11"><g fill="#f5b50a"><use href="#st"/><use href="#st" x="12.5"/><use href="#st" x="25"/><use href="#st" x="37.5"/><use href="#st" x="50"/></g></svg></div>
    <span class="quote-mark">”</span>
    <q>"The speed and professionalism of the Harbor Work team is unmatched. They filled a critical role for us in record time when other agencies struggled. Highly recommended."</q>
    <div class="quote-name">Luis Carver</div>
    <div class="quote-role">Operations Manager, Freightwise Co.</div>
  </article>
</section>

<section>
  <div class="abs cta-seek cta-block">
    <div class="inner">
      <h2 style="color:#fff">Ready to Find Your Next Role?</h2>
      <p style="color:#c7cbd6">Browse thousands of job opportunities across Canada and take the next step in your career journey.</p>
      <span class="btn btn-gold">Browse Jobs</span>
    </div>
  </div>
  <div class="abs cta-hire cta-block">
    <div class="inner">
      <h2 style="color:var(--navy)">Looking to Hire Top Talent?</h2>
      <p style="color:var(--navy)">Connect with qualified professionals who are ready to contribute to your company's success.</p>
      <span class="btn" style="border:1px solid var(--deep);color:var(--deep)">Post a Job</span>
    </div>
  </div>
</section>

<footer class="abs site-footer">
  <div class="foot-brand"><strong>HARBORWORK</strong><small>RECRUITMENT AGENCY</small></div>
  <p class="foot-about">Connecting exceptional talent with leading organizations across Canada. We specialize in finding the perfect fit for both candidates and employers.</p>
  <div class="socials"><i></i><i></i><i></i></div>

  <div class="foot-col" style="left:417px">
    <h4>Quick Links</h4>
    <ul><li>→ Home</li><li>→ About Us</li><li>→ For Candidates</li><li>→ For Employers</li><li>→ Vancouver Office</li><li>→ Contact Us</li></ul>
  </div>
  <div class="foot-col" style="left:615px">
    <h4>Our Services</h4>
    <ul><li>Oil, Gas &amp; Mining</li><li>Administrative</li><li>Construction &amp; Trades</li><li>Warehouse &amp; Logistics</li><li>Manufacturing</li></ul>
  </div>
  <div class="foot-col foot-contact" style="left:813px">
    <h4>Contact Us</h4>
    <ul>
      <li><svg width="11" height="11" viewBox="0 0 11 11" fill="none" stroke="#f5b50a"><path d="M5.5 10S9 7 9 4.5a3.5 3.5 0 00-7 0C2 7 5.5 10 5.5 10z"/><circle cx="5.5" cy="4.5" r="1.2"/></svg><span>48 Commerce Row, Suite<br>210<br>Vancouver, BC V5K 2C7</span></li>
      <li><svg width="11" height="11" viewBox="0 0 11 11" fill="none" stroke="#f5b50a"><path d="M2 1.5h2l1 2.5-1.3 1a6 6 0 002.3 2.3l1-1.3 2.5 1v2A1 1 0 018.5 10 8 8 0 011 2.5a1 1 0 011-1z"/></svg><span>+1 (604) 555-0187</span></li>
      <li><svg width="11" height="11" viewBox="0 0 11 11" fill="none" stroke="#f5b50a"><rect x="1" y="2.5" width="9" height="6.5" rx=".8"/><path d="M1 3l4.5 3.3L10 3"/></svg><span>hello@harborwork.ca</span></li>
    </ul>
  </div>

  <div class="foot-bottom">
    <span>© 2026 Harbor Work Agency. All rights reserved.</span>
    <nav><span>Terms of Use</span><span>Privacy Policy</span><span>Disclaimer</span></nav>
  </div>
</footer>

</body>
</html>
```